Stationery Design Project

We are a packaging machinery manufacturer that mainly serve the food industry.
We now require a full set of stationary including name card, envelop, letter paper, and etc. to match our company image. The logo has been awarded in a previous contest which is attached here.
Updates
Project Deadline Extended
Reason: We have extended the deadline. We have adjusted the deadline before launch to avoid confusion but it turns out the new date wasn't implemented by the system. All designers please feel free to submit your design. Thank you!
Target Market(s)
B2B customer, including decision maker in food factories, chemical factories, etc.
Industry/Entity Type
Industry
Colors
Designer to choose colors to be used in the design.
Look and feel
Each slider illustrates characteristics of the customer's brand and the style your logo design should communicate.

```html
<!DOCTYPE html>
<html lang="en">
<head>
<meta charset="utf-8">
<title>Varnok Stationery Set</title>
<link rel="stylesheet" href="https://fonts.googleapis.com/css2?family=Open+Sans:wght@300;400;600;700&display=swap">
<style>
:root{
  --green:#0b6b34;
  --green-dark:#075a2a;
  --grey:#8a9095;
  --grey-light:#9ea3a7;
  --stage:#80878b;
  --paper:#ffffff;
  --ink:#2b2b2b;
}
*{margin:0;padding:0;box-sizing:border-box}
html,body{width:1200px;height:1071px;overflow:hidden}
body{background:var(--stage);font-family:"Open Sans",Arial,sans-serif;color:var(--ink);position:relative}
.piece{position:absolute;background:var(--paper)}
.brand{display:flex;align-items:center;gap:8px;color:var(--green);font-weight:700;line-height:1}
.brand-square{background:var(--green);display:block}
.contact{font-size:7.5px;line-height:9.5px;color:#444}
.contact b{color:var(--green);font-weight:600}
.contact .firm{color:var(--green);font-weight:700;font-size:8px;margin-bottom:7px}

/* letterhead */
.letterhead{left:83px;top:78px;width:498px;height:705px}
.letterhead .brand{position:absolute;left:45px;top:66px;font-size:38px}
.letterhead .brand-square{width:30px;height:30px}
.letterhead .divider{position:absolute;left:250px;top:65px;width:1px;height:43px;background:var(--green)}
.letterhead .contact{position:absolute;left:260px;top:63px}
.mission-title{position:absolute;left:0;width:406px;top:224px;text-align:center;font-weight:300;font-size:18px;color:#333}
.mission-body{position:absolute;left:45px;top:272px;width:402px;font-size:12.2px;line-height:15px;text-align:justify;color:#222}
.signature{position:absolute;left:368px;top:540px;width:82px;height:28px;background:#f1f1f1}
.signer{position:absolute;left:366px;top:575px;font-size:5.5px;color:#555}
.letter-footer{position:absolute;left:0;top:653px;width:498px;height:26px}
.letter-footer .url{position:absolute;left:42px;top:6px;font-size:10px;color:#fff;font-weight:600}

/* business card front */
.card-front{left:712px;top:114px;width:335px;height:206px;overflow:hidden}
.card-front svg{position:absolute;left:0;top:0}
.card-front .brand{position:absolute;left:23px;top:25px;font-size:24px;color:#fff}
.card-front .brand-square{width:18px;height:18px;background:#fff}
.card-front .address{position:absolute;left:23px;top:124px;font-size:8.5px;line-height:11.5px;color:#fff}
.card-front .lines{position:absolute;left:23px;top:153px;font-size:8.5px;line-height:12px;color:#fff;list-style:none}
.card-front .lines li{display:flex;align-items:center;gap:6px}
.card-front .lines svg{position:static}
.card-front .holder{position:absolute;right:14px;top:95px;text-align:right}
.holder .name{font-size:14px;font-weight:600;color:#1e1e1e;line-height:16px}
.holder .role{font-size:11.5px;color:#fff;line-height:14px}
.card-front .tab{position:absolute;right:0;top:98px;width:7px;height:25px;background:var(--green);border-radius:3px 0 0 3px}

/* business card back */
.card-back{left:712px;top:397px;width:335px;height:205px}
.card-back .brand{position:absolute;left:54px;top:74px;font-size:52px;gap:12px}
.card-back .brand-square{width:40px;height:40px}
.card-back .band{position:absolute;left:0;top:176px;width:335px;height:17px;background:var(--grey-light);color:#fff;font-size:11px;text-align:center;line-height:17px}

/* envelope front */
.envelope-front{left:285px;top:813px;width:408px;height:205px}
.envelope-front .brand{position:absolute;left:25px;top:20px;font-size:30px}
.envelope-front .brand-square{width:23px;height:23px}
.envelope-front .rule{position:absolute;left:28px;top:120px;width:1px;height:42px;background:var(--green)}
.envelope-front .contact{position:absolute;left:35px;top:117px;font-size:6px;line-height:7.6px}
.envelope-front .contact .firm{font-size:6.5px;margin-bottom:6px}
.envelope-front .band{position:absolute;left:0;top:182px;width:408px;height:23px;background:var(--green)}

/* envelope back */
.envelope-back{left:724px;top:675px;width:406px;height:286px;background:transparent}
.envelope-back svg{position:absolute;left:0;top:0}
.envelope-back .brand{position:absolute;left:268px;top:232px;font-size:19px;gap:5px}
.envelope-back .brand-square{width:14px;height:14px}
</style>
</head>
<body>

<section class="piece letterhead" aria-label="Letterhead">
  <div class="brand"><span class="brand-square"></span>VARNOK</div>
  <span class="divider"></span>
  <div class="contact">
    <div class="firm">VARNOK PACKAGING TECHNOLOGY</div>
    <div><b>Tel:</b> 555-0142-7731</div>
    <div><b>Mobile:</b> +555-019-8226</div>
    <div><b>Email:</b> info@varnok.com</div>
  </div>
  <h2 class="mission-title">OUR MISSION</h2>
  <p class="mission-body">Lorem ipsum dolor sit amet, consectetur adipiscing elit. Donec orci purus, luctus vitae dignissim eu, iaculis sed purus. Vivamus faucibus, ipsum nec aliquet viverra, leo mauris condimentum ligula, sit amet sagittis enim ligula quis arcu. Nam egestas tortor id nisi porttitor mattis. In tortor ante, ultricies in suscipit a, tempus non massa. Vivamus et auctor mi. Fusce vel massa nulla. Phasellus nec eros mauris, et scelerisque orci. Donec malesuada orci vitae nulla accumsan porta a id massa. Quisque accumsan iaculis magna sit amet fringilla. Maecenas consequat, magna eget tincidunt semper, odio nibh rutrum mi, id feugiat ante nisi eu risus. Vestibulum nunc orci, rhoncus a placerat in, ultricies in mi. Cras mattis varius eros, vel fringilla nisi suscipit eget.</p>
  <div class="signature" role="img" aria-label="Handwritten signature of the co-founder"></div>
  <div class="signer">Lena Marsh, Co-Founder &amp; CEO</div>
  <div class="letter-footer">
    <svg width="498" height="26" viewBox="0 0 498 26">
      <polygon points="0,0 250,0 237,13 250,26 0,26" fill="var(--green)"/>
      <polygon points="256,0 498,0 498,26 256,26 243,13" fill="var(--grey)"/>
    </svg>
    <span class="url">www.varnokpackaging.com</span>
  </div>
</section>

<section class="piece card-front" aria-label="Business card front">
  <svg width="335" height="206" viewBox="0 0 335 206">
    <rect width="335" height="206" fill="#fff"/>
    <polygon points="0,0 233,0 128,103 228,206 0,206" fill="var(--green)"/>
    <polygon points="308,0 335,0 335,206 300,206 200,103" fill="var(--grey)"/>
  </svg>
  <div class="brand"><span class="brand-square"></span>VARNOK</div>
  <p class="address">21, Lorem ipsum, Nunc<br>eget sagittis augue,</p>
  <ul class="lines">
    <li><svg width="7" height="7" viewBox="0 0 10 10"><path d="M2 1l2 2-1 1.5c.8 1.4 1.7 2.3 3 3L7.5 6l2 2-1.5 1.5C4 9 1 6 .5 2z" fill="#fff"/></svg>555 0142 7731</li>
    <li><svg width="7" height="7" viewBox="0 0 10 10"><rect x="2.5" y="0.5" width="5" height="9" rx="1" fill="none" stroke="#fff"/></svg>555 0198 2264</li>
    <li><svg width="7" height="7" viewBox="0 0 10 10"><rect x="0.5" y="2" width="9" height="6" fill="#fff"/></svg>info@varnok.com</li>
  </ul>
  <div class="holder"><div class="name">Your Name</div><div class="role">Director</div></div>
  <span class="tab"></span>
</section>

<section class="piece card-back" aria-label="Business card back">
  <div class="brand"><span class="brand-square"></span>VARNOK</div>
  <div class="band">www.varnokpackaging.com</div>
</section>

<section class="piece envelope-front" aria-label="Envelope front">
  <div class="brand"><span class="brand-square"></span>VARNOK</div>
  <span class="rule"></span>
  <div class="contact">
    <div class="firm">VARNOK PACKAGING TECHNOLOGY</div>
    <div><b>Tel:</b> 555-0142-7731</div>
    <div><b>Mobile:</b> +555-019-8226</div>
    <div><b>Email:</b> info@varnok.com</div>
    <div><b>Website:</b> www.varnokpackaging.com</div>
  </div>
  <div class="band"></div>
</section>

<section class="piece envelope-back" aria-label="Envelope back">
  <svg width="406" height="286" viewBox="0 0 406 286">
    <defs>
      <linearGradient id="flap" x1="0" y1="0" x2="0" y2="1">
        <stop offset="0" stop-color="#0e7a3d"/>
        <stop offset="1" stop-color="var(--green-dark)"/>
      </linearGradient>
    </defs>
    <rect width="406" height="286" fill="#fff"/>
    <polygon points="0,0 406,0 406,96 382,140 24,140 0,96" fill="url(#flap)"/>
    <polygon points="24,140 382,140 406,286 0,286" fill="#f7f7f7"/>
  </svg>
  <div class="brand"><span class="brand-square"></span>VARNOK</div>
</section>

</body>
</html>
```